Web Design Project - KornHaus.de

The page shall provide individual brown-bread mix.
There shall be presented:
* RECIPES: consumer's choice and feedback area
* EQUIPMENT: baking equipment store
* BREAD-MIX: individual mix and configurator function for bread-mix
The consumer can search/view the content and checkout the products. A user can establish a profile. A user can interact on the page for feedback on content and connection to social media.

```html
<!DOCTYPE html>
<html lang="en">
<head>
<meta charset="utf-8">
<title>KornHaus – Brown-bread mix</title>
<link rel="stylesheet" href="https://fonts.googleapis.com/css2?family=Arimo:wght@400;700&family=PT+Sans+Narrow:wght@700&display=swap">
<style>
:root{
  --cream:#f3e2c8;
  --cream-light:#fbf3e6;
  --brand:#c57a1f;
  --brand-dark:#a86a22;
  --nav:#b5762c;
  --headline-light:#d2a863;
  --headline:#c3922f;
  --accent-red:#d3221a;
  --text:#1e1e1e;
  --muted:#6b6b6b;
  --white:#ffffff;
}
*{box-sizing:border-box;margin:0;padding:0}
html,body{width:1200px;height:982px;overflow:hidden;background:var(--white)}
body{position:relative;font-family:"Arimo",Arial,sans-serif;color:var(--text)}
a{text-decoration:none;color:inherit}

.site-header{position:absolute;left:0;top:0;width:1200px;height:185px;
  background:radial-gradient(ellipse at 25% 10%,var(--cream-light) 0%,var(--cream) 75%);}
.brand{position:absolute;left:110px;top:30px}
.brand-name{font-family:"Arimo",Arial,sans-serif;font-weight:700;font-size:58px;letter-spacing:-1.5px;color:var(--brand);line-height:1}
.brand-tagline{position:absolute;left:138px;top:64px;white-space:nowrap;font-weight:700;font-size:17px;color:var(--muted)}

.account{position:absolute;right:120px;top:24px;display:flex;align-items:center;gap:10px;font-weight:700;font-size:19px;color:var(--nav)}
.social{display:flex;align-items:center;gap:5px;font-size:12px;font-weight:400}
.social-square{width:12px;height:12px;background:var(--brand-dark)}
.account .divider{width:2px;height:22px;background:var(--nav)}
.account .social + .social{margin-right:8px}

.main-nav{position:absolute;left:111px;top:138px;display:flex;gap:33px;font-weight:700;font-size:19.5px;color:var(--nav)}
.search{position:absolute;left:784px;top:133px;width:304px;height:34px;border-radius:17px;background:var(--white);
  box-shadow:inset 0 1px 3px rgba(160,110,40,.35);display:flex;align-items:center;padding:0 14px 0 17px;
  font-size:14px;color:var(--nav)}
.search span{flex:1}

.hero{position:absolute;left:0;top:185px;width:1200px;height:340px;
  background:linear-gradient(to bottom,var(--white) 0,var(--white) 293px,#f6ece0 300px,var(--white) 340px)}
.hero-photo{position:absolute;left:117px;top:22px;width:494px;height:296px;border-radius:8px;
  background:radial-gradient(ellipse at 50% 45%,#c98a45 0%,#b57439 40%,#e3c08f 75%,#f7ecdb 100%)}
.hero-title{position:absolute;left:595px;top:46px;font-family:"PT Sans Narrow","Arial Narrow",sans-serif;font-weight:700;
  font-size:55px;line-height:56px;letter-spacing:-1.5px;color:var(--headline-light)}
.hero-title .line-two{display:block;margin-left:43px;color:var(--headline)}
.hero-text{position:absolute;left:653px;top:170px;width:410px;font-size:14.5px;line-height:23px;color:#111}
.learn-more{display:inline-flex;align-items:center;gap:7px;font-weight:700;font-size:16.5px;color:var(--accent-red)}
.hero .learn-more{position:absolute;left:911px;top:229px}

.features{position:absolute;left:0;top:525px;width:1200px;display:block}
.feature{position:absolute;top:0;width:310px}
.feature-photo{height:195px;border-radius:6px}
.feature-title{position:absolute;top:215px;font-weight:700;font-size:20px;color:var(--brand-dark)}
.feature-text{position:absolute;top:249px;width:305px;font-size:11.6px;line-height:17px}
.feature .learn-more{position:absolute;top:316px}
.feature--mix{left:120px}
.feature--mix .feature-photo{width:295px;background:radial-gradient(ellipse at 45% 60%,#c8a268 0%,#dcc08c 45%,#fbf6ee 80%)}
.feature--equipment{left:459px}
.feature--equipment .feature-photo{margin-left:52px;width:200px;background:radial-gradient(ellipse at 45% 50%,#8d8f92 0%,#b8b9bb 45%,#f4f4f4 85%)}
.feature--recipes{left:787px}
.feature--recipes .feature-photo{margin-left:18px;width:240px;background:radial-gradient(ellipse at 50% 50%,#2fb264 0%,#d9c19a 55%,#fbf8f2 85%)}
.feature .feature-title,.feature .feature-text,.feature .learn-more{left:6px}

.site-footer{position:absolute;left:0;top:918px;width:1200px;height:64px;
  background:linear-gradient(to bottom,var(--cream) 0%,var(--cream-light) 100%);font-size:14px;color:var(--brand-dark)}
.copyright{position:absolute;left:110px;top:26px}
.footer-nav{position:absolute;right:121px;top:26px;display:flex;gap:20px;align-items:center}
.footer-nav .social{font-size:11px}
</style>
</head>
<body>
<header class="site-header">
  <div class="brand">
    <div class="brand-name">KornHaus</div>
    <div class="brand-tagline">Brown-bread mix</div>
  </div>
  <div class="account">
    <a class="social" href="#"><span class="social-square"></span>Chirper</a>
    <a class="social" href="#"><span class="social-square"></span>Friendbook</a>
    <a href="#">Join Now</a><span class="divider"></span><a href="#">Login</a>
  </div>
  <nav class="main-nav">
    <a href="#">About KornHaus</a><a href="#">Bread-Mix</a><a href="#">Equipment</a><a href="#">Recipes</a><a href="#">Contact</a>
  </nav>
  <div class="search">
    <span>search, product, recipe</span>
    <svg width="18" height="18" viewBox="0 0 18 18" aria-hidden="true"><circle cx="7.5" cy="7.5" r="5.5" fill="none" stroke="#e2b98a" stroke-width="2"/><line x1="11.5" y1="11.5" x2="16" y2="16" stroke="#e2b98a" stroke-width="2.5" stroke-linecap="round"/></svg>
  </div>
</header>

<section class="hero">
  <div class="hero-photo" role="img" aria-label="Basket of assorted breads, rolls and sliced loaf on a wooden board"></div>
  <h1 class="hero-title">Eat The Smart<span class="line-two">Way with KornHaus</span></h1>
  <p class="hero-text">Lorem ipsum dolor sit amet, consectetur adipisicing elit, sed do eiusmod tempor incididunt ut labore et dolore magna</p>
  <a class="learn-more" href="#">LEARN MORE
    <svg width="16" height="16" viewBox="0 0 16 16" aria-hidden="true"><circle cx="8" cy="8" r="6.5" fill="none" stroke="#d3221a" stroke-width="2.2"/><path d="M5 8h5M8 5.2 10.8 8 8 10.8" fill="none" stroke="#d3221a" stroke-width="2.2"/></svg></a>
</section>

<section class="features">
  <article class="feature feature--mix">
    <div class="feature-photo" role="img" aria-label="Bundle of wheat ears with spilled grain"></div>
    <h2 class="feature-title">Bread-Mix</h2>
    <p class="feature-text">Lorem ipsum dolor sit amet, consectetur adipisicing elit, sed do eiusmod tempor incididunt ut labore et dolore magna aliqua. Ut enim ad minim veniam, quis</p>
    <a class="learn-more" href="#">LEARN MORE
      <svg width="16" height="16" viewBox="0 0 16 16" aria-hidden="true"><circle cx="8" cy="8" r="6.5" fill="none" stroke="#d3221a" stroke-width="2.2"/><path d="M5 8h5M8 5.2 10.8 8 8 10.8" fill="none" stroke="#d3221a" stroke-width="2.2"/></svg></a>
  </article>
  <article class="feature feature--equipment">
    <div class="feature-photo" role="img" aria-label="Steel bread machine beside slices of brown bread"></div>
    <h2 class="feature-title">Equipment</h2>
    <p class="feature-text">Lorem ipsum dolor sit amet, consectetur adipisicing elit, sed do eiusmod tempor incididunt ut labore et dolore magna aliqua. Ut enim ad minim veniam, quis</p>
    <a class="learn-more" href="#">LEARN MORE
      <svg width="16" height="16" viewBox="0 0 16 16" aria-hidden="true"><circle cx="8" cy="8" r="6.5" fill="none" stroke="#d3221a" stroke-width="2.2"/><path d="M5 8h5M8 5.2 10.8 8 8 10.8" fill="none" stroke="#d3221a" stroke-width="2.2"/></svg></a>
  </article>
  <article class="feature feature--recipes">
    <div class="feature-photo" role="img" aria-label="Green recipe notebook with wooden spoons"></div>
    <h2 class="feature-title">Recipes</h2>
    <p class="feature-text">Lorem ipsum dolor sit amet, consectetur adipisicing elit, sed do eiusmod tempor incididunt ut labore et dolore magna aliqua. Ut enim ad minim veniam, quis</p>
    <a class="learn-more" href="#">LEARN MORE
      <svg width="16" height="16" viewBox="0 0 16 16" aria-hidden="true"><circle cx="8" cy="8" r="6.5" fill="none" stroke="#d3221a" stroke-width="2.2"/><path d="M5 8h5M8 5.2 10.8 8 8 10.8" fill="none" stroke="#d3221a" stroke-width="2.2"/></svg></a>
  </article>
</section>

<footer class="site-footer">
  <p class="copyright">© 2011 KornHaus, All Rights Reserved</p>
  <nav class="footer-nav">
    <a href="#">About KornHaus</a><a href="#">Bread-Mix</a><a href="#">Equipment</a><a href="#">Recipes</a><a href="#">Contact</a>
    <a class="social" href="#"><span class="social-square"></span>Chirper</a>
    <a class="social" href="#"><span class="social-square"></span>Friendbook</a>
  </nav>
</footer>
</body>
</html>
```